Private practice for psychiatry and psychotherapy needs a business card and logo

I need a logo and business card design for my private practice for psychiatry and psychotherapy. The optional names for my practice are: Vornhoute Praktijk voor Psychiatrie en Psychotherapie, or short: Praktijk Vornhoute.
I am a (child and adolescent) psychiatrist and psychotherapist. I diagnose and treat infants, children, adolescents and adults with psychiatric symptoms/disorders. I also give supervision to colleagues about their own treatments. My work is characterised by personal involvement, transparence, creativity and professionality.
I would like to have an appealing, light and bright, yet basic design that invites people (both children and adults) to contact me, gives trust and hope, without loosing professional appearance.
I uploaded my contact information which should not necessarily be all included (in this form) on the card as long as people know how to contact me. Please feel free to be creative!
Please note that my website is only temporarely and need a new design and update too!

Target Market(s)

Clients and patients (children, adolescents, adults) with psychiatric symptoms who need diagnosis and treatment. I work with private clients and patients through medical insurances.

Industry/Entity Type

Mental Health

Contact Information for Business Card

Dr. Sanne Vornhoute-ter Kuilen
Psychiater/Kinder- en Jeugdpsychiater
Wouter Heskampstraat 14
3071 PX Rotterdam
t: 06-51928764
e: info@praktijkvornhoute.nl
i: www.praktijkvornhoute.nl

Logo Text

Praktijk Vornhoute voor Psychiatrie en Psychotherapie; or short: Praktijk Vornhoute

Font styles to use
Sans Serif
Other font styles liked:
• up to designer

Requirements
Must have
• Appealing, light, bright, creative, trustful, professional and unique.

```html
<!DOCTYPE html>
<html lang="nl">
<head>
<meta charset="utf-8">
<title>Praktijk Vornhoute – visitekaartje</title>
<link rel="stylesheet" href="https://fonts.googleapis.com/css2?family=Source+Sans+3:wght@400;600;700&display=swap">
<style>
  :root {
    --backdrop: #333333;
    --card: #ffffff;
    --green: #5fa41c;
    --red: #ee1d23;
    --grey-text: #5a5a5a;
    --grey-sub: #6d6d6d;
    --ring-faint: #eef3e7;
  }
  * { margin: 0; padding: 0; box-sizing: border-box; }
  html, body { width: 1200px; height: 900px; overflow: hidden; }
  body {
    background: var(--backdrop);
    font-family: "Source Sans 3", "Myriad Pro", Arial, sans-serif;
    position: relative;
  }
  .card {
    position: absolute;
    top: 271px;
    width: 457px;
    height: 281px;
    background: var(--card);
    border-radius: 16px;
    overflow: hidden;
    box-shadow: 3px 4px 6px rgba(0,0,0,0.55);
  }
  .card--front { left: 137px; }
  .card--back { left: 606px; }
  .faint-ring { position: absolute; top: 0; left: 0; width: 457px; height: 281px; }

  .practice-heading {
    position: absolute; left: 27px; top: 27px;
    color: var(--green); font-weight: 700; text-align: center;
    line-height: 1.15;
  }
  .practice-heading .line-1 { font-size: 19.5px; display: block; }
  .practice-heading .line-2 { font-size: 15.5px; display: block; }

  .person { position: absolute; left: 27px; top: 126px; }
  .person__name { font-size: 17px; font-weight: 700; letter-spacing: 0.1px; }
  .person__name .first { color: var(--red); }
  .person__name .last { color: var(--green); }
  .person__role { font-size: 13px; color: var(--grey-text); margin-top: 5px; }

  .contact { position: absolute; left: 27px; top: 186px; font-size: 13px; color: var(--grey-text); }
  .contact p { margin-bottom: 7px; }
  .contact .label { color: var(--red); font-weight: 700; }
  .contact .sep { display: inline-block; width: 1px; height: 14px; background: var(--grey-text); margin: 0 5px; vertical-align: -2px; }
  .contact .address { margin-top: 11px; }

  .brand {
    position: absolute; left: 0; right: 0; top: 82px;
    text-align: center;
  }
  .brand__dot {
    display: block; width: 68px; height: 68px; border-radius: 50%;
    background: var(--green); margin: 0 auto 19px;
  }
  .brand__name {
    color: var(--green); font-weight: 700; font-size: 17px; line-height: 1.2;
  }
</style>
</head>
<body>
  <section class="card card--front">
    <svg class="faint-ring" viewBox="0 0 457 281" aria-hidden="true">
      <circle cx="467" cy="139" r="118" fill="none" stroke="var(--ring-faint)" stroke-width="24"/>
    </svg>
    <h1 class="practice-heading">
      <span class="line-1">PRAKTIJK VORNHOUTE VOOR</span>
      <span class="line-2">Psychiatrie en Psychotherapie</span>
    </h1>
    <div class="person">
      <p class="person__name"><span class="first">DR. SANNE VORNHOUTE-</span><span class="last"> TER KUILEN</span></p>
      <p class="person__role">Psychiater/kinder- en jeugdpsychiater</p>
    </div>
    <div class="contact">
      <p><span class="label">P:</span> 06-51928764<span class="sep"></span><span class="label">E:</span> info@praktijkvornhoute.nl</p>
      <p><span class="label">W:</span> www.praktijkvornhoute.nl</p>
      <p class="address">Wouter Heskampstraat 14 , 3071 PX Rotterdam</p>
    </div>
  </section>

  <section class="card card--back">
    <svg class="faint-ring" viewBox="0 0 457 281" aria-hidden="true">
      <circle cx="-2" cy="139" r="118" fill="none" stroke="var(--ring-faint)" stroke-width="24"/>
    </svg>
    <div class="brand">
      <span class="brand__dot"></span>
      <p class="brand__name">Praktijk Vornhoute voor<br>Psychiatrie en Psychotherapie</p>
    </div>
  </section>
</body>
</html>
```